Business Card Re-Design for a Lighting Designer

I would like my business card re-designed. It is currently high gloss and they scratch too easily. I don not think the current design lends itself well to a matte finish. I have included the current design for reference along with our company logo.
Check out our website for current branding.
http://www.brambleorchidstudio.example

Updates
Some of the top contenders are muslim and it is a holiday for them. I do not want to discriminate and would expect the same courtesy for holidays we celebrate.
Target Market(s)
Interior Designers, Architects
Contact Information for Business Card
Logo - Name, Title, Address, Telephone Number and Extension, Email
Font styles to use
Requirements
Must have
- All the information listed on the current business card. If you use Red, it needs to be the red from our logo.
Nice to have
- Vertical and Horizontal Designs will be entertained.
Should not have
- Requirements for a glossy finish...should not look too corporate since we are a design firm.

```html
<!DOCTYPE html>
<html lang="en">
<head>
<meta charset="utf-8">
<title>Bramble Orchid Studio – Business Card</title>
<link href="https://fonts.googleapis.com/css2?family=Poppins:wght@300;400;700&display=swap" rel="stylesheet">
<style>
  :root {
    --brand-red: #a00d0d;
    --ink: #1e1e1e;
    --muted: #555555;
    --paper: #ffffff;
    --card-black: #1f2124;
    --light-text: #f2f2f2;
    --backdrop: #d9d4cc;
  }
  html, body {
    margin: 0;
    padding: 0;
    width: 1200px;
    height: 1040px;
    overflow: hidden;
    background: var(--backdrop);
    font-family: "Poppins", sans-serif;
  }
  .canvas {
    position: relative;
    width: 1200px;
    height: 1040px;
  }
  .card {
    position: absolute;
    width: 640px;
    height: 366px;
    box-shadow: 0 12px 30px rgba(0,0,0,0.25);
    overflow: hidden;
  }
  /* Front */
  .card-front {
    left: 70px;
    top: 70px;
    background: var(--paper);
  }
  .corner-triangle {
    position: absolute;
    left: 0;
    bottom: 0;
  }
  .wordmark {
    position: absolute;
    right: 40px;
    top: 46px;
    display: flex;
    align-items: center;
    gap: 14px;
  }
  .wordmark-square {
    width: 22px;
    height: 22px;
    background: var(--brand-red);
  }
  .wordmark-name {
    font-weight: 300;
    font-size: 30px;
    line-height: 1;
    color: var(--ink);
    letter-spacing: 1px;
    text-transform: uppercase;
  }
  .tagline {
    position: absolute;
    right: 40px;
    top: 96px;
    font-weight: 300;
    font-size: 11px;
    letter-spacing: 2px;
    color: var(--muted);
    text-transform: uppercase;
  }
  .identity {
    position: absolute;
    left: 44px;
    top: 150px;
  }
  .person-name {
    margin: 0;
    font-weight: 700;
    font-size: 24px;
    color: var(--brand-red);
    text-transform: uppercase;
    letter-spacing: 0.5px;
  }
  .person-title {
    margin: 2px 0 0;
    font-weight: 400;
    font-size: 15px;
    color: var(--ink);
  }
  .contact {
    position: absolute;
    left: 270px;
    top: 196px;
    font-weight: 300;
    font-size: 12.5px;
    line-height: 1.45;
    color: var(--muted);
  }
  .contact p { margin: 0; }
  .contact b { font-weight: 700; color: var(--ink); }
  .rule {
    position: absolute;
    left: 270px;
    right: 0;
    top: 306px;
    height: 2px;
    background: var(--brand-red);
  }
  .site-front {
    position: absolute;
    left: 270px;
    top: 314px;
    font-weight: 300;
    font-size: 12.5px;
    color: var(--muted);
  }
  /* Back */
  .card-back {
    left: 490px;
    top: 600px;
    background: var(--card-black);
  }
  .site-back {
    position: absolute;
    left: 26px;
    top: 0;
    bottom: 0;
    display: flex;
    align-items: center;
    writing-mode: vertical-rl;
    font-weight: 400;
    font-size: 11px;
    letter-spacing: 2px;
    color: var(--light-text);
    text-transform: uppercase;
    white-space: nowrap;
  }
  .back-mark {
    position: absolute;
    left: 0;
    right: 0;
    top: 0;
    bottom: 0;
    display: flex;
    align-items: center;
    justify-content: center;
    gap: 14px;
  }
  .back-mark .wordmark-name { color: var(--light-text); }
</style>
</head>
<body>
<main class="canvas">
  <section class="card card-front" aria-label="Business card front">
    <svg class="corner-triangle" width="60" height="40" viewBox="0 0 60 40" aria-hidden="true">
      <polygon points="0,0 60,40 0,40" fill="var(--brand-red)"/>
    </svg>
    <div class="wordmark">
      <span class="wordmark-square"></span>
      <span class="wordmark-name">Bramble Orchid</span>
    </div>
    <div class="tagline">Lighting for Architecture</div>
    <div class="identity">
      <h1 class="person-name">Maren Holloway</h1>
      <p class="person-title">Principal</p>
    </div>
    <div class="contact">
      <p>212 Fernbrook Lane, Cedar Falls</p>
      <p>Suite 40, Ohio 44010 USA</p>
      <p><b>P</b> : 555.014.2230 x1</p>
      <p><b>E</b> : maren@brambleorchidstudio.example</p>
    </div>
    <div class="rule"></div>
    <div class="site-front">brambleorchidstudio.example</div>
  </section>

  <section class="card card-back" aria-label="Business card back">
    <div class="site-back">www.brambleorchidstudio.example</div>
    <div class="back-mark">
      <span class="wordmark-square"></span>
      <span class="wordmark-name">Bramble Orchid</span>
    </div>
  </section>
</main>
</body>
</html>
```